Coffeeshop menu for filter tip

We want to have a cannabis (coffeeshop) menu in the size 25mm wide x 60mm wide. Some examples attached.

it must have the following text:
Menu

WEED p/g
Vortigan €16
Tangerosa €14
Dusk Rover €14
Mangolina €16
Ultra Fern €14
Amber Hermit €14

HASH p/g
Nepali Bronze €12
Velvet Ember€11
Cedar Pine €14
Red Fable €10

Target Market(s)

tourist in Amsterdam

Requirements
Nice to have
• cannabis sign leaf
• No Cigarettes allowed symbol

```html
<!DOCTYPE html>
<html lang="en">
<head>
<meta charset="utf-8">
<title>Coffee Shop Menu</title>
<link rel="stylesheet" href="https://fonts.googleapis.com/css2?family=Gilda+Display&family=Oswald:wght@600&family=Tinos:wght@700&display=swap">
<style>
  :root {
    --bg-light: #1d4a42;
    --bg-mid: #0f2b27;
    --bg-dark: #050d0c;
    --ink: #ffffff;
    --ink-soft: #d9dcdc;
    --steel: #b4babd;
    --gold: #f7e816;
    --red: #d4121a;
    --red-deep: #6a0a0c;
    --leaf-a: #8fe6b8;
    --leaf-b: #1f8a58;
  }
  * { margin: 0; padding: 0; box-sizing: border-box; }
  html, body { width: 1200px; height: 2884px; overflow: hidden; background: var(--bg-dark); }
  .menu-card {
    position: relative;
    width: 1200px; height: 2884px;
    overflow: hidden;
    background:
      radial-gradient(ellipse 900px 1200px at 300px 500px, var(--bg-light) 0%, var(--bg-mid) 45%, transparent 80%),
      linear-gradient(180deg, var(--bg-mid) 0%, #0a1d1a 50%, var(--bg-dark) 100%);
    font-family: "Gilda Display", "Times New Roman", serif;
    color: var(--ink);
  }
  .leaf-mark {
    position: absolute; left: 620px; top: 0; width: 580px; height: 690px;
    background: radial-gradient(ellipse at 55% 45%, var(--leaf-a) 0%, var(--leaf-b) 45%, rgba(15,43,39,0) 75%);
    opacity: .85;
  }
  .shop-label {
    position: absolute; left: 24px; top: 68px;
    font-size: 84px; letter-spacing: 3px; color: var(--ink-soft);
    text-shadow: 0 4px 8px rgba(0,0,0,.6);
  }
  .rule {
    position: absolute; height: 6px;
    background: linear-gradient(90deg, rgba(255,255,255,.9), rgba(255,255,255,.5));
  }
  .rule--short { left: 0; top: 192px; width: 760px; }
  .rule--full { left: 0; top: 620px; width: 1200px; height: 5px; background: linear-gradient(90deg, rgba(255,255,255,.8), rgba(255,255,255,.2) 70%, rgba(255,255,255,.6)); }
  .menu-title {
    position: absolute; left: 62px; top: 262px;
    font-family: "Oswald", "Arial Narrow", sans-serif; font-weight: 600;
    font-size: 250px; line-height: 1; color: var(--steel);
    transform: scaleX(.95); transform-origin: left;
    text-shadow: 0 8px 14px rgba(0,0,0,.5);
  }
  .section-head {
    position: absolute; left: 52px;
    font-family: "Tinos", "Times New Roman", serif; font-weight: 700;
    font-size: 222px; line-height: 1; color: var(--gold);
    -webkit-text-stroke: 10px var(--red);
    paint-order: stroke fill;
    text-shadow: 0 0 18px var(--red-deep), 0 0 30px rgba(212,18,26,.7);
    white-space: nowrap;
  }
  .section-head--weed { top: 676px; }
  .section-head--hash { top: 1720px; }
  .price-frame {
    position: absolute; left: 22px; top: 944px; width: 1152px; height: 1694px;
    border: 5px solid var(--ink); border-top: none;
  }
  .price-list { position: absolute; left: 66px; width: 1078px; list-style: none; }
  .price-list--weed { top: 936px; }
  .price-list--hash { top: 1978px; }
  .price-item {
    display: flex; justify-content: space-between;
    font-size: 110px; line-height: 124px; color: var(--ink);
    text-shadow: 0 6px 10px rgba(0,0,0,.85);
    white-space: nowrap;
  }
  .price-list--hash .price-item { font-size: 116px; line-height: 162px; }
  .notice {
    position: absolute; left: 50px; top: 2680px;
    font-size: 74px; color: var(--ink-soft);
  }
  .no-smoking { position: absolute; left: 658px; top: 2558px; width: 272px; height: 272px; }
</style>
</head>
<body>
<main class="menu-card">
  <div class="leaf-mark" role="img" aria-label="Green cannabis leaf emblem"></div>
  <div class="shop-label">COFFEE SHOP</div>
  <div class="rule rule--short"></div>
  <h1 class="menu-title">MENU</h1>
  <div class="rule rule--full"></div>

  <div class="section-head section-head--weed">WEED p/g</div>
  <div class="price-frame"></div>
  <ul class="price-list price-list--weed">
    <li class="price-item"><span>Vortigan</span><span>€16</span></li>
    <li class="price-item"><span>Tangerosa</span><span>€14</span></li>
    <li class="price-item"><span>Dusk Rover</span><span>€14</span></li>
    <li class="price-item"><span>Mangolina</span><span>€16</span></li>
    <li class="price-item"><span>Ultra Fern</span><span>€14</span></li>
    <li class="price-item"><span>Amber Hermit</span><span>€14</span></li>
  </ul>

  <div class="section-head section-head--hash">HASH p/g</div>
  <ul class="price-list price-list--hash">
    <li class="price-item"><span>Nepali Bronze</span><span>€12</span></li>
    <li class="price-item"><span>Velvet Ember</span><span>€11</span></li>
    <li class="price-item"><span>Cedar Pine</span><span>€14</span></li>
    <li class="price-item"><span>Red Fable</span><span>€10</span></li>
  </ul>

  <div class="notice">No Cigarettes</div>
  <svg class="no-smoking" viewBox="0 0 272 272" role="img" aria-label="No smoking sign">
    <circle cx="136" cy="136" r="128" fill="#ffffff"/>
    <rect x="40" y="128" width="150" height="30" fill="#1a1a1a"/>
    <rect x="194" y="128" width="14" height="30" fill="#1a1a1a"/>
    <rect x="212" y="128" width="14" height="30" fill="#1a1a1a"/>
    <path d="M200 120 c-10 -20 20 -30 6 -56 M218 120 c-10 -20 20 -30 6 -56" fill="none" stroke="#1a1a1a" stroke-width="8"/>
    <circle cx="136" cy="136" r="116" fill="none" stroke="#e3121b" stroke-width="26"/>
    <line x1="54" y1="54" x2="218" y2="218" stroke="#e3121b" stroke-width="26"/>
  </svg>
</main>
</body>
</html>
```